Updated ebook fantasy cover with feathered dragon and twisted tail

Ebook designs are a specific type of layout. They must be at least partially legible at thumbnail size on Brindlecart, and interesting enough to draw the eye of a modern fantasy book reader.

Before you begin, I have an extensive collection of my likes and a few critiques of other covers on a pinwarble board.
http://www.snipboard-example.net/moxlavender/brookstone-cover-ideas/

Let me also say that the story is not scary, it is set in a gorgeous natural environment on planet earth, and I do not want monsterous dragons. The dragon is the good guy, he talks, and his best friend is a fairy. Think cuddly.

As for colors, I am trying to attract young women. They are drawn to beautiful images like those you see on my pinwarble board. To help, I have chosen some colors below, but you don't have to use them all. As for the pop of color. Use your design instincts.

The following text must fit on the cover.
Thimble A Wyvern Chronicle (title- should be readable at thumbnail size)
Songs of the Meridian (series title)
Lucinda Marsh Hadley (author)

The hero of the book and the subject of the cover is a dragon with:
*A long corkscrew like tail
*Feathered wings (black with white lower edges)
*Black feathers covering his chest (over lungs) but the rest is scales. (scales need not be overly obvious.
*A large, indigo (not Aqua) blue crest of feathers like a cockatiel (see attached photo)
*A thin line of feathers snaking up the back of the neck*
*Workable arms (no T Rex issues)
*An intelligent and even gentle appearance
*No large horns
*Body is black with highlights that can be blue or whatever color works best in the setting
*Striking blue eyes that appear kind rather than fierce

This dragon should be what you imagine as a precursor to the birds of today. You will see what I mean on my pinwarble board, or ask questions. I prefer focused covers with a warm color palette NO MONOTONE or washed out layouts, please. The entire dragon does not need to appear. The winning design will lean toward whimsy, but not juvenile.

If you are looking for a background, consider
*a light filled forest
*a beach at sunset (but not in the water)
*near a waterfall
*near a lake
*a mountain peak
*or a simple, light colored, elegantly textured background
You may have other ideas.

Design should be a minimum of 300 dpi at 6 x 9 inches

I feel that I may have confused you.
Elegant
Beautiful
Inviting
Charming
Sweet
These are words that should describe the cover.

You may use either illustration, stock photos, or any combination.

The topography should be striking, easy to read and creative.

I expect a controlled and thoughtfully placed pop of color to draw the eye to the title or the dragon.

If you are looking for a way to introduce color, consider adding
* the northern lights (Aurora)
*colorful gemstones or crystals
*a colorful band of ripped tapestry, but the dragon should not seem to be in possession of the tapestry.
Another idea is below.

Extra consideration will be given to designs that are large enough to extend onto the spine of a 6 x 9 book for a 300 page printvale book. Ask for exact dimensions if interested.

Two more elements can be considered for addition.
*A Cairn (think a pile of rocks)
*A small, beautiful wingless fairy like creature (they are best friends) I prefer that she not be represented in her complete form, but perhaps her hand reaching out to the dragon as her sleeve drapes in some pop of color. She has long, wavy brown hair. You could show her from the back, perhaps dressed in a cloak.

This is the blurb:
"Every dragon dreams of entering the Cairn—but not as a murder victim.

Velmo, the dragon with the twisted tail, is summoned home to the lair by a sweet and familiar voice. “Bring the trollkin known as Moss to me or all will be lost,” she beckons. Except, Velmo has already fulfilled his destiny, and he has no reason to risk his life, yet again. Still, nobody denies an Elemental, and certainly not a dragon of the Garnet clan. But is she calling him home to die, or will he expose the brutal killer before he becomes the next victim?

Thimble: A Wyvern Chronicle penetrates the world of dragons, a society filled with smoke and lies where honorable wishes are warped by vague memories and unfathomable greed. "

This will be a relaunch and it is part of a trilogy so I am very interested in working with the same designer for all three. The first book features a female troll and the third the creature that you can think of as a beautiful fairy without wings. So this one project could well lead to three.

I have added a cairn photo that I purchased from Snapcrate and an idea of what I mean by a twisted tail, but it should fit the dragon and not be as thin as a snake.

To see the cover as it is today: Hint, I do like my current topography, but think it could be even better.
http://www.brindlecart-example.com/Thimble-Wyvern-Chronicle-Songs-Meridian-ebook/dp/Q77K2WXNPL/ref=sr_1_4?ie=UTF8&qid=1520947715&sr=8-4&keywords=marsh+hadley

After reviewing more of the amazing designs created by the designers on this site, I have decided to both guarantee and increase the budget for my project. I look forward to seeing the designs from the designers who have already accepted, and any others who may have been on the fence about accepting the challenge. I feel confident that one of you will create a design that will whack me to my knees, and for that, you will deserve a larger reward. If you are interested, start at my pinwarble board for my likes and dislikes. http://www.snipboard-example.net/moxlavender/brookstone-cover-ideas/

Reason: My updated (and clarified) brief drew more interested designers, and to to be fair, I have decided to extend the deadline by a few days. I am very interested to see all your designs so take more time if you need it. I am offering detailed feedback to anyone who requests it.

Target Market(s)

Young adult, primarily female, 15+. A reader of fantasy. The dragon is the primary element.

Industry/Entity Type

Environment

Font styles to use
Other font styles liked:
• I like Trajon Pro, but perhaps add script to add some elegance i

Colors
fee18a
fcf9ce
0255a3
ffc214
faa54b
9bcb3c
f68d4d

Requirements
Must have
• some or all of the dragon described above
a pop of color
professional font treatment
Interesting at thumbnail size as seen on Brindlecart
Nice to have
• the fairy like creature described above in a loving pose with the dragon
the rock pile,
I am not telling you what color to use, but I don't like pastels, I do like warm colors or greens
Should not have
• cartoonish features.
unreadable font.
Monotone color scheme. large blocks of color that seem to exist only to hold the text.
Setting that could not exist on this planet
Excessive fire

```html
<!DOCTYPE html>
<html lang="en">
<head>
<meta charset="utf-8">
<title>Thimble A Wyvern Chronicle — Cover Wrap</title>
<link rel="stylesheet" href="https://fonts.googleapis.com/css2?family=Bebas+Neue&family=Oswald:wght@400;500&family=Roboto+Condensed:wght@400&display=swap">
<style>
  :root {
    --stage: #e6e6e6;
    --ink: #0b0608;
    --ink-plum: #2a0c22;
    --ember-soft: rgba(214, 128, 30, 0.55);
    --plum-glow: rgba(110, 30, 90, 0.55);
    --gold-light: #ffd84a;
    --gold: #f2b414;
    --gold-deep: #a86f06;
    --gold-haze: rgba(242, 180, 20, 0.35);
    --paper-white: #f1ece6;
    --body-grey: #bdb6b2;
    --panel: rgba(0, 0, 0, 0.55);
    --slot: #222023;
    --dragon-rose: rgba(214, 110, 140, 0.55);
    --dragon-plum: rgba(120, 50, 120, 0.35);
  }

  * { box-sizing: border-box; margin: 0; padding: 0; }

  html, body {
    width: 1200px;
    height: 800px;
    overflow: hidden;
    background: var(--stage);
  }

  .cover-wrap {
    position: absolute;
    left: 150px;
    top: 80px;
    width: 900px;
    height: 640px;
    display: flex;
  }

  .panel {
    position: relative;
    height: 100%;
    overflow: hidden;
    background:
      radial-gradient(ellipse 45% 30% at 85% 42%, var(--ember-soft), transparent 70%),
      radial-gradient(ellipse 40% 35% at 10% 82%, var(--ember-soft), transparent 70%),
      radial-gradient(ellipse 60% 40% at 70% 20%, var(--plum-glow), transparent 75%),
      radial-gradient(ellipse 60% 50% at 20% 40%, var(--plum-glow), transparent 75%),
      linear-gradient(180deg, var(--ink-plum), var(--ink) 55%, var(--ink-plum));
  }

  /* ---------- back cover ---------- */
  .back-cover {
    width: 430px;
    padding: 30px 28px 0 32px;
  }

  .back-series {
    font-family: "Oswald", sans-serif;
    font-size: 15px;
    letter-spacing: 1.5px;
    color: var(--paper-white);
    text-transform: uppercase;
  }

  .back-title {
    font-family: "Bebas Neue", sans-serif;
    font-weight: 400;
    font-size: 32px;
    line-height: 1;
    margin-top: 2px;
    color: var(--gold);
    letter-spacing: 0.5px;
  }

  .back-author {
    font-family: "Oswald", sans-serif;
    font-size: 12px;
    letter-spacing: 1px;
    color: var(--paper-white);
    text-align: right;
    margin-top: 4px;
    padding-right: 6px;
    text-transform: uppercase;
  }

  .back-blurb {
    margin-top: 20px;
    padding: 6px 8px;
    background: var(--panel);
    font-family: "Roboto Condensed", sans-serif;
    font-size: 10.4px;
    line-height: 13.6px;
    color: var(--body-grey);
    text-align: justify;
  }

  .back-slots {
    position: absolute;
    left: 32px;
    right: 28px;
    bottom: 28px;
    display: flex;
    justify-content: space-between;
  }

  .back-slot {
    width: 104px;
    height: 48px;
    background: var(--slot);
    display: flex;
    align-items: center;
    justify-content: center;
    font-family: "Oswald", sans-serif;
    font-size: 10px;
    letter-spacing: 1px;
    color: var(--paper-white);
  }

  /* ---------- spine ---------- */
  .spine {
    width: 40px;
    display: flex;
    flex-direction: column;
    align-items: center;
    padding-top: 20px;
    border-left: 1px solid rgba(255,255,255,0.06);
    border-right: 1px solid rgba(0,0,0,0.6);
  }

  .spine-title {
    writing-mode: vertical-rl;
    font-family: "Bebas Neue", sans-serif;
    font-size: 30px;
    letter-spacing: 2px;
    color: var(--gold);
    line-height: 1;
  }

  .spine-author {
    writing-mode: vertical-rl;
    margin-top: 36px;
    font-family: "Oswald", sans-serif;
    font-size: 8px;
    letter-spacing: 1px;
    color: var(--paper-white);
    text-transform: uppercase;
  }

  /* ---------- front cover ---------- */
  .front-cover {
    width: 430px;
    text-align: center;
  }

  .front-series {
    margin-top: 14px;
    font-family: "Oswald", sans-serif;
    font-weight: 500;
    font-size: 15px;
    letter-spacing: 2.5px;
    color: var(--paper-white);
    text-transform: uppercase;
  }

  .front-title {
    font-weight: 400;
  }

  .gold-type {
    display: block;
    background: linear-gradient(180deg, var(--gold-light) 0%, var(--gold) 45%, var(--gold-deep) 100%);
    -webkit-background-clip: text;
    background-clip: text;
    color: transparent;
  }

  .front-title-main {
    font-family: "Bebas Neue", sans-serif;
    font-size: 138px;
    line-height: 0.9;
    margin-top: 6px;
    letter-spacing: 2px;
  }

  .front-title-joint {
    position: relative;
    display: block;
    height: 46px;
    margin-top: 4px;
  }

  .wing-ornament {
    position: absolute;
    left: 135px;
    top: 2px;
    width: 160px;
    height: 30px;
    border-radius: 4px;
    background: radial-gradient(ellipse 50% 50% at 50% 50%, var(--gold-haze), transparent 80%);
  }

  .front-title-a {
    position: absolute;
    left: 0;
    right: 0;
    top: 14px;
    font-family: "Bebas Neue", sans-serif;
    font-size: 36px;
    line-height: 1;
  }

  .front-title-sub {
    font-family: "Bebas Neue", sans-serif;
    font-size: 50px;
    line-height: 1;
    margin-top: 4px;
    letter-spacing: 1px;
  }

  .front-author {
    margin-top: 8px;
    font-family: "Oswald", sans-serif;
    font-weight: 500;
    font-size: 15px;
    letter-spacing: 1.5px;
    color: var(--paper-white);
    text-transform: uppercase;
  }

  .dragon-art {
    position: absolute;
    left: 110px;
    top: 330px;
    width: 270px;
    height: 310px;
    background:
      radial-gradient(ellipse 50% 50% at 55% 55%, var(--dragon-rose), transparent 75%),
      radial-gradient(ellipse 40% 30% at 40% 25%, var(--dragon-plum), transparent 80%);
  }
</style>
</head>
<body>
  <main class="cover-wrap">
    <section class="panel back-cover">
      <p class="back-series">Songs of the Meridian</p>
      <h2 class="back-title">Thimble A Wyvern Chronicle</h2>
      <p class="back-author">Lucinda Marsh Hadley</p>
      <p class="back-blurb">Lorem ipsum dolor sit amet, consectetur adipisicing elit, sed do eiusmod tempor incididunt ut labore et dolore magna aliqua. Ut enim ad minim veniam, quis nostrud exercitation. Lorem ipsum dolor sit amet, consectetur adipisicing elit, sed do eiusmod tempor incididunt ut labore et dolore magna aliqua. Ut enim ad minim veniam, quis nostrud exercitation. Lorem ipsum dolor sit amet, consectetur adipisicing elit, sed do eiusmod tempor incididunt ut labore et dolore magna aliqua. Ut enim ad minim veniam, quis nostrud exercitation. Lorem ipsum dolor sit amet, consectetur adipisicing elit, sed do eiusmod tempor incididunt ut labore et dolore magna aliqua. Ut enim ad minim veniam, quis nostrud exercitation. Lorem ipsum dolor sit amet, consectetur adipisicing elit, sed do eiusmod tempor incididunt ut labore et dolore magna aliqua. Ut enim ad minim veniam, quis nostrud exercitation. Lorem ipsum dolor sit amet, consectetur adipisicing elit, sed do eiusmod tempor incididunt ut labore et dolore magna aliqua. Ut enim ad minim veniam, quis nostrud exercitation. Lorem ipsum dolor sit amet, consectetur adipisicing elit, sed do eiusmod tempor incididunt ut labore et dolore magna aliqua. Ut enim ad minim veniam, quis nostrud exercitation. Lorem ipsum dolor sit amet, consectetur adipisicing elit, sed do eiusmod tempor incididunt ut labore et dolore magna aliqua. Ut enim ad minim veniam, quis nostrud exercitation.</p>
      <div class="back-slots">
        <div class="back-slot">LOGO</div>
        <div class="back-slot">ISBN</div>
      </div>
    </section>

    <section class="panel spine">
      <p class="spine-title">Thimble A Wyvern Chronicle</p>
      <p class="spine-author">Lucinda Marsh Hadley</p>
    </section>

    <section class="panel front-cover">
      <p class="front-series">Songs of the Meridian</p>
      <h1 class="front-title">
        <span class="front-title-main gold-type">Thimble</span>
        <span class="front-title-joint">
          <span class="wing-ornament" role="img" aria-label="Pair of small golden feathered wings framing the letter A"></span>
          <span class="front-title-a gold-type">A</span>
        </span>
        <span class="front-title-sub gold-type">Wyvern Chronicle</span>
      </h1>
      <p class="front-author">Lucinda Marsh Hadley</p>

      <div class="dragon-art" role="img" aria-label="Illustration of a pink-scaled dragon with a purple feather crest and a long curving neck"></div>
    </section>
  </main>
</body>
</html>
```